Business Card Design Project - The Bridgeway Partners

Company Name - The Bridgeway Partners

We need a unique logo and business cards

We are a team of experienced IT professionals who specialize in providing business value to organizations via the analysis and understanding the challenges of your particular organization. We focus on understanding the challenges first, and execute against your priorities partnering with your highly valued key resources.

Our extensive experience and focus on Agile delivery methodologies help our clients continuously improve and deliver quality solutions. Using this approach we will always deliver the greatest return on your investments.

Target Market(s)

Large organizations IT departments

Industry/Entity Type

Business

Font styles to use
Serif
Sans Serif

Requirements
Should not have
• no pictures

```html
<!DOCTYPE html>
<html lang="en">
<head>
<meta charset="utf-8">
<title>The Bridgeway Partners – Business Card</title>
<link rel="stylesheet" href="https://fonts.googleapis.com/css2?family=Open+Sans:wght@400;600&display=swap">
<style>
  :root {
    --backdrop: #1b1b1b;
    --card-edge: #f2f2f0;
    --card-face: #3b3b3b;
    --accent: #f0921e;
    --ink-light: #e9e9e9;
    --rule: #f2f2f2;
  }
  * { margin: 0; padding: 0; box-sizing: border-box; }
  html, body {
    width: 1200px;
    height: 757px;
    overflow: hidden;
    background: var(--backdrop);
    font-family: "Open Sans", Arial, sans-serif;
  }
  .canvas {
    position: relative;
    width: 1200px;
    height: 757px;
  }
  .business-card {
    position: absolute;
    left: 145px;
    top: 118px;
    width: 910px;
    height: 520px;
    background: var(--card-edge);
    padding: 24px;
  }
  .card-face {
    position: relative;
    width: 100%;
    height: 100%;
    background: var(--card-face);
  }
  .brand-name {
    position: absolute;
    left: 48px;
    top: 200px;
    width: 330px;
    font-size: 27px;
    font-weight: 600;
    letter-spacing: 0.5px;
    color: var(--ink-light);
    white-space: nowrap;
  }
  .divider {
    position: absolute;
    left: 402px;
    top: 70px;
    width: 4px;
    height: 250px;
    background: var(--rule);
  }
  .contact-block {
    position: absolute;
    left: 440px;
    top: 72px;
  }
  .person-name {
    font-size: 22px;
    font-weight: 600;
    color: var(--accent);
    line-height: 1.1;
  }
  .person-role {
    font-size: 15px;
    color: var(--ink-light);
    margin-bottom: 10px;
  }
  .contact-list {
    list-style: none;
  }
  .contact-item {
    display: flex;
    align-items: center;
    gap: 22px;
    margin-bottom: 22px;
    font-size: 16px;
    color: var(--ink-light);
  }
  .contact-dot {
    width: 24px;
    height: 24px;
    border-radius: 50%;
    background: var(--accent);
    flex-shrink: 0;
  }
</style>
</head>
<body>
<main class="canvas">
  <section class="business-card">
    <div class="card-face">
      <div class="brand-name">The Bridgeway Partners</div>
      <div class="divider"></div>
      <div class="contact-block">
        <p class="person-name">Dana Morrow</p>
        <p class="person-role">Manager</p>
        <ul class="contact-list">
          <li class="contact-item"><span class="contact-dot"></span>00 555 204 318 00</li>
          <li class="contact-item"><span class="contact-dot"></span>www.bridgewaypartners.com</li>
          <li class="contact-item"><span class="contact-dot"></span>email:hello@bridgewaypartners.com</li>
        </ul>
      </div>
    </div>
  </section>
</main>
</body>
</html>
```